A-Stand Directional Sign Design

Objective:
We need a professional graphic design for an A-Stand sign that will guide customers arriving in our parking lot to our office. The design should be visually clear, welcoming, and aligned with our brand identity.
REQUIREMENTS:
Two versions of the design:
- One with an arrow pointing left
- One with an arrow pointing right
(This allows us to place the A-Stand anywhere and flip the graphic as needed.)
DIMENSIONS:
- Viewable Area: 30" x 40"
BRAND ALIGNMENT:
- Colors, fonts, and overall style should match our website: www.skornabel.com
- Clean, modern, and professional look consistent with our aviation/tourism brand
CONTENT:
- Clear directional arrow (left or right depending on version)
- Text: “Office Entrance” or similar concise wording (designers may propose alternatives if they improve clarity)
READABILITY:
- Bold, high-contrast design for visibility from a distance
- Simple layout that avoids clutter
DELIVERABLES:
- Final artwork in print-ready format (PDF preferred)
- Two versions: Arrow Left and Arrow Right
DESIGN GOAL:
Ensure customers can easily find our office upon arrival, while reinforcing skorNABEL’s professional and welcoming brand image.
Target Market(s)
Tourism

```html
<!DOCTYPE html>
<html lang="en">
<head>
<meta charset="utf-8">
<title>skorNABEL A-Stand Directional Signs</title>
<link href="https://fonts.googleapis.com/css2?family=Michroma&display=swap" rel="stylesheet">
<style>
  :root {
    --page: #ffffff;
    --deep-teal: #0f2e36;
    --mid-teal: #437f87;
    --sky-light: #9fd0d6;
    --sky-mid: #5fa3ab;
    --sky-deep: #2b6770;
    --sunset: #d9782a;
    --sunset-dark: #6b3512;
    --cabin: #4d8fa0;
    --cabin-dark: #1f3f47;
    --white: #ffffff;
    --brand-blue: #2a6fbd;
  }
  * { margin: 0; padding: 0; box-sizing: border-box; }
  html, body {
    width: 1200px; height: 1000px; overflow: hidden;
    background: var(--page);
  }
  .canvas { position: relative; width: 1200px; height: 1000px; }

  .sign {
    position: absolute; top: 204px;
    width: 446px; height: 595px;
    overflow: hidden;
    background: var(--mid-teal);
  }
  .sign--left { left: 110px; }
  .sign--right { left: 646px; }

  .sign__column {
    position: absolute; left: 0; top: 0;
    width: 223px; height: 100%;
    background: var(--deep-teal);
  }
  .sign__hero-photo {
    position: absolute; left: 0; top: 0;
    width: 100%; height: 380px;
    background: linear-gradient(180deg, var(--sky-light) 0%, var(--sky-mid) 45%, var(--sky-deep) 75%, rgba(67,127,135,0) 100%);
  }
  .sign__hero-fade {
    position: absolute; left: 0; top: 0;
    width: 223px; height: 380px;
    background: linear-gradient(180deg, rgba(15,46,54,0.05) 0%, rgba(15,46,54,0.25) 55%, var(--deep-teal) 100%);
  }

  .gallery { position: absolute; left: 281px; top: 120px; }
  .gallery__photo {
    width: 107px; height: 71px; margin-bottom: 23px;
  }
  .gallery__photo--sunset { background: linear-gradient(135deg, var(--sunset) 0%, var(--sunset-dark) 100%); }
  .gallery__photo--window { background: linear-gradient(90deg, #d7e4e8 0%, #8ea4a8 55%, #4a3c30 100%); }
  .gallery__photo--cockpit { background: linear-gradient(180deg, var(--cabin) 0%, var(--cabin-dark) 100%); }
  .gallery__photo--crew { background: linear-gradient(90deg, #7a5a40 0%, #2c2a28 50%, #c9d3d6 100%); }

  .brand {
    position: absolute; left: 22px; top: 410px; width: 180px;
    text-align: center;
  }
  .brand__name {
    font-family: "Michroma", sans-serif;
    font-size: 19px; color: var(--white);
    letter-spacing: 0.5px;
  }

  .direction {
    position: absolute; left: 66px; top: 521px;
    width: 312px; height: 41px;
  }
  .direction__label {
    position: absolute; inset: 0;
    display: flex; align-items: center; justify-content: center;
    font-family: "Michroma", sans-serif;
    font-size: 19px; color: var(--brand-blue);
    letter-spacing: 0.3px;
  }
</style>
</head>
<body>
<main class="canvas">

  <section class="sign sign--left" aria-label="Sign with arrow pointing left">
    <div class="sign__column"></div>
    <div class="sign__hero-photo" role="img" aria-label="Photo of a white helicopter flying over a coastal city with passengers seated on the skids"></div>
    <div class="sign__hero-fade"></div>
    <div class="gallery">
      <div class="gallery__photo gallery__photo--sunset" role="img" aria-label="Photo of a helicopter silhouetted against an orange sunset sky"></div>
      <div class="gallery__photo gallery__photo--window" role="img" aria-label="Photo of a passenger with headset looking out over a city"></div>
      <div class="gallery__photo gallery__photo--cockpit" role="img" aria-label="Photo of a cockpit view over a coastline"></div>
      <div class="gallery__photo gallery__photo--crew" role="img" aria-label="Photo of smiling passengers wearing headsets inside a helicopter"></div>
    </div>
    <div class="brand"><p class="brand__name">SKORNABEL</p></div>
    <div class="direction">
      <svg width="312" height="41" viewBox="0 0 312 41" aria-hidden="true">
        <polygon points="0,20.5 20,0 312,0 292,20.5 312,41 20,41" fill="#ffffff"/>
      </svg>
      <span class="direction__label">OFFICE ENTRANCE</span>
    </div>
  </section>

  <section class="sign sign--right" aria-label="Sign with arrow pointing right">
    <div class="sign__column"></div>
    <div class="sign__hero-photo" role="img" aria-label="Photo of a white helicopter flying over a coastal city with passengers seated on the skids"></div>
    <div class="sign__hero-fade"></div>
    <div class="gallery">
      <div class="gallery__photo gallery__photo--sunset" role="img" aria-label="Photo of a helicopter silhouetted against an orange sunset sky"></div>
      <div class="gallery__photo gallery__photo--window" role="img" aria-label="Photo of a passenger with headset looking out over a city"></div>
      <div class="gallery__photo gallery__photo--cockpit" role="img" aria-label="Photo of a cockpit view over a coastline"></div>
      <div class="gallery__photo gallery__photo--crew" role="img" aria-label="Photo of smiling passengers wearing headsets inside a helicopter"></div>
    </div>
    <div class="brand"><p class="brand__name">SKORNABEL</p></div>
    <div class="direction">
      <svg width="312" height="41" viewBox="0 0 312 41" aria-hidden="true">
        <polygon points="0,0 292,0 312,20.5 292,41 0,41 20,20.5" fill="#ffffff"/>
      </svg>
      <span class="direction__label">OFFICE ENTRANCE</span>
    </div>
  </section>

</main>
</body>
</html>
```